依頼詳細
トップページのデザイン トップページとサブページ(2ページ目以降)のデザイン サブページは、トップページのデザインを引き継ぐ感じで
グローバルナビ  ワードプレス×レスポンシブで制作予定

全体的なイメージ https://www.morino-kobo.jp/index.html
青とホワイトを基調にした清潔感があり ごちゃごちゃしすぎず
患者さんの視線で見やすく 探しやすい感じを希望します。
お子様や女性にも好まれるような可愛いイラストなどもお願いします。

グローバルナビに入れる予定の項目 Q&A、アクセス、医院紹介、治療内容、マウスピース矯正、費用、部分矯正、裏側矯正

トップページに記載したい文章
マウスピース型矯正装置(クリアフィット)をメインの紹介するサイト
裏側矯正にも力入れており、見えないMIX (マウスピース矯正と裏側矯正の組み合わせで幅広く対応できる。

最新式 デジタルスキャナー dento scope の紹介
参考https://hanawa-dent.jp/orthodontic/clearfit/

ブログ形式で 新着情報
休診日・診療時間/
ご相談・お問い合わせ

希望イメージ
シンプル 複雑
単色 カラフル
暗い 明るい
日常 高級
遊び心 厳粛
未来的 伝統的
女性的 男性的
希望する色
水色系
納品ファイル
• 高解像度JPG (.jpg)
• フォトショップ形式 (.psd)
補足説明
マウスピース矯正を マウスピース型矯正装置
クリアフィット をマウスピース型矯正装置(クリアフィット)

※医療広告の関係で表記を統一してください。
用語は、マウスピース型矯正装置(クリアフィット)を徹底してください。

高校生~20代女性に響くような デザインが希望です。

透明で見ないこと 取り外せること
最新式 3Dスキャンナー dento scoopeを導入していること
dento scope により、簡易シュミレーションが見れること
裏側矯正も得意なことから 組み合わせることによって対応できる
幅が広がったこと。

を強調したデザインが希望です。

参照https://www.kirari-ha.jp/simulation/

なるべく裏側矯正の内容は、記載しないでマウスピース型矯正装置(クリアフィット)の内容だけにしたい。

よろしくお願いします。

```html
<!DOCTYPE html>
<html lang="ja">
<head>
<meta charset="UTF-8">
<title>日本橋浜町ルミエ矯正歯科</title>
<link href="https://fonts.googleapis.com/css2?family=M+PLUS+Rounded+1c:wght@400;500;700;800&family=Noto+Sans+JP:wght@400;500;700&display=swap" rel="stylesheet">
<style>
:root{
  --blue:#6fc0e0;
  --blue-soft:#e6f3fa;
  --blue-pale:#f2f9fd;
  --navy:#1f3557;
  --text:#3a4656;
  --muted:#7d8896;
  --accent:#f2a79d;
  --peach:#fbefe9;
  --white:#ffffff;
  --line:#d5e3ec;
}
*{box-sizing:border-box;margin:0;padding:0}
html,body{width:1200px;height:4013px;overflow:hidden}
body{position:relative;background:var(--white);color:var(--text);font-family:"Noto Sans JP",sans-serif;font-size:15px;line-height:1.8}
.abs{position:absolute}
.round{font-family:"M PLUS Rounded 1c",sans-serif}

/* header */
.brand{left:120px;top:24px;width:280px;text-align:center}
.brand-mark{width:40px;height:40px;border-radius:50%;background:var(--blue-soft);border:3px solid var(--blue);margin:0 auto 6px}
.brand-name{font-family:"M PLUS Rounded 1c",sans-serif;font-weight:700;font-size:22px;color:var(--navy);line-height:1.3}
.tel-box{left:60px;top:166px}
.tel-label{font-size:14px;color:var(--muted)}
.tel-number{display:flex;align-items:center;gap:8px;font-family:"M PLUS Rounded 1c",sans-serif;font-weight:800;font-size:34px;color:var(--blue);line-height:1.2;white-space:nowrap}
.quick-link{width:120px;height:120px;border-radius:50% 46% 52% 48%;display:flex;flex-direction:column;align-items:center;justify-content:center;font-size:14px;color:var(--navy);font-weight:500}
.quick-qa{left:70px;top:270px;background:#fbe2dc}
.quick-access{left:200px;top:300px;background:var(--blue-soft)}
.global-nav{left:410px;top:30px;display:flex;gap:6px}
.nav-item{width:124px;text-align:center;font-size:14px;color:var(--navy)}
.nav-item svg{display:block;margin:0 auto 6px}

/* hero */
.hero-blob{left:460px;top:0;width:740px;height:780px;background:var(--blue-pale);border-radius:0 0 0 380px}
.hero-photo{left:540px;top:160px;width:660px;height:580px;border-radius:290px 0 0 200px;background:linear-gradient(135deg,#dbeff8,#b8dcec 55%,#eef6fa)}
.hero-copy{left:370px;top:150px;writing-mode:vertical-rl;font-family:"M PLUS Rounded 1c",sans-serif;font-weight:700;font-size:28px;color:var(--navy);letter-spacing:.08em;line-height:1.6;height:420px;white-space:nowrap}
.hero-copy .hl{color:var(--blue)}

/* schedule */
.schedule{left:48px;top:560px;width:560px;border-collapse:collapse;background:var(--white);font-size:14px}
.schedule th,.schedule td{border:1px solid var(--line);text-align:center;height:44px}
.schedule thead th{background:var(--navy);color:var(--white);font-weight:500}
.schedule td.time{width:150px}

/* about */
.about-bg{left:0;top:820px;width:1200px;height:1200px;background:var(--blue-pale);border-radius:0 300px 0 260px}
.sec-title{display:flex;align-items:center;gap:14px;font-family:"M PLUS Rounded 1c",sans-serif;font-weight:700;color:var(--navy)}
.about-title{left:110px;top:880px;font-size:30px}
.about-title .bar{width:20px;height:34px;background:var(--accent);border-radius:4px}
.about-title small{font-size:20px;color:var(--text);font-weight:500}
.about-text{left:60px;top:1010px;width:580px;font-size:15px;line-height:2}
.about-text p{margin-bottom:22px}
.about-photo{left:690px;top:900px;width:470px;height:380px;border-radius:200px 200px 40px 200px;background:linear-gradient(140deg,#e8f1f6,#c9dce6 60%,#f4f8fa)}
.merit-title{left:0;top:1340px;width:1200px;text-align:center;font-size:22px;justify-content:center}
.merit-grid{left:120px;top:1410px;width:960px;display:grid;grid-template-columns:repeat(3,300px);column-gap:30px;row-gap:26px}
.merit{display:flex;gap:12px;align-items:center}
.merit-photo{flex:0 0 150px;height:112px;border-radius:8px;background:linear-gradient(135deg,#e9f2f7,#cfe2ec)}
.merit p{font-size:14px;line-height:1.6;color:var(--text)}
.btn{display:flex;align-items:center;justify-content:space-between;height:52px;border:2px solid var(--navy);border-radius:4px;padding:0 20px;font-weight:700;font-size:16px;color:var(--navy);background:var(--white)}
.more-about{left:120px;top:1880px;width:290px}

/* scanner */
.scanner-title{left:120px;top:2150px;font-size:26px}
.scanner-title small{font-size:20px;font-weight:500}
.scanner-photo{left:80px;top:2290px;width:400px;height:400px;border-radius:50%;background:radial-gradient(circle at 50% 50%,#f3f6f8,#dde7ee 70%,#fbe7e1)}
.scanner-text{left:620px;top:2300px;width:540px;font-size:15px;line-height:2}
.more-scanner{left:520px;top:2510px;width:310px}

/* news */
.news-bg{left:0;top:2680px;width:1200px;height:640px;background:var(--peach);border-radius:300px 0 0 0}
.news-title{left:0;top:2820px;width:1200px;justify-content:center;font-size:28px}
.news-list{left:80px;top:2920px;display:flex;gap:30px}
.post{width:240px;background:var(--white);box-shadow:0 2px 8px rgba(31,53,87,.1)}
.post-thumb{height:220px;background:linear-gradient(135deg,#d7e7ef,#a9c3cf)}
.post-thumb.logo{display:flex;flex-direction:column;align-items:center;justify-content:center;background:var(--white);gap:10px}
.post-thumb.logo .mark{width:56px;height:56px;border-radius:50%;background:#cfe9c9}
.post-thumb.logo span{font-family:"M PLUS Rounded 1c",sans-serif;font-weight:700;font-size:16px;color:#5aa06a}
.post-thumb.red{background:linear-gradient(135deg,#c45555,#e9a7a1)}
.post-body{padding:12px 16px 18px;font-size:13px;line-height:1.6;height:92px}
.post-date{color:var(--muted);font-size:12px}
.arrow{width:50px;height:50px;border-radius:50%;background:#8a8f96;display:flex;align-items:center;justify-content:center;top:3005px}
.news-more{left:930px;top:3260px;width:200px;height:40px;font-size:13px;font-weight:500;border-width:1px}

/* footer */
.foot-brand{left:120px;top:3350px;display:flex;align-items:center;gap:12px}
.foot-brand .brand-mark{margin:0;width:34px;height:34px}
.foot-brand .brand-name{font-size:22px}
.foot-address{left:130px;top:3410px;font-size:13px;color:var(--muted)}
.foot-tel{left:120px;top:3440px;font-size:52px}
.foot-tel svg{width:44px;height:44px}
.cta{top:3455px;width:270px;height:64px;background:var(--navy);color:var(--white);border-radius:4px;display:flex;align-items:center;justify-content:center;gap:16px;font-weight:700;font-size:17px}
.map{left:0;top:3540px;width:1200px;height:320px;background:linear-gradient(135deg,#e5ece7,#d8e2ea 50%,#eef0e6)}
.footer{left:0;top:3860px;width:1200px;height:153px;background:var(--navy);color:var(--white)}
.footer-nav{display:flex;justify-content:center;gap:0;padding-top:22px;font-size:14px}
.footer-nav span{padding:0 32px;border-left:1px solid rgba(255,255,255,.3)}
.footer-nav span:first-child{border-left:none}
.footer-mark{width:26px;height:26px;border-radius:50%;border:2px solid var(--white);margin:26px auto 8px}
.copy{text-align:center;font-size:12px;opacity:.85}
</style>
</head>
<body>

<div class="abs hero-blob"></div>
<div class="abs hero-photo" role="img" aria-label="歯科衛生士の女性と子どもが笑顔で歯を見せる写真"></div>

<header>
  <div class="abs brand">
    <div class="brand-mark"></div>
    <div class="brand-name">日本橋浜町<br>ルミエ矯正歯科</div>
  </div>
  <nav class="abs global-nav round">
    <div class="nav-item"><svg width="40" height="40" viewBox="0 0 40 40" fill="none" stroke="#1f3557" stroke-width="2"><rect x="8" y="6" width="24" height="28" rx="3"/><line x1="13" y1="14" x2="27" y2="14"/><line x1="13" y1="20" x2="27" y2="20"/><line x1="13" y1="26" x2="22" y2="26"/></svg>医院紹介</div>
    <div class="nav-item"><svg width="40" height="40" viewBox="0 0 40 40" fill="none" stroke="#1f3557" stroke-width="2"><line x1="8" y1="32" x2="28" y2="12"/><circle cx="30" cy="10" r="4"/></svg>治療内容</div>
    <div class="nav-item"><svg width="40" height="40" viewBox="0 0 40 40" fill="none" stroke="#1f3557" stroke-width="2"><path d="M6 16c4-6 24-6 28 0c-2 10-6 14-14 14S8 26 6 16z"/></svg>マウスピース矯正</div>
    <div class="nav-item"><svg width="40" height="40" viewBox="0 0 40 40" fill="none" stroke="#1f3557" stroke-width="2"><path d="M10 8c6-4 14-4 20 0c2 8-2 24-5 24s-3-10-5-10s-2 10-5 10S8 16 10 8z"/></svg>部分矯正</div>
    <div class="nav-item"><svg width="40" height="40" viewBox="0 0 40 40" fill="none" stroke="#1f3557" stroke-width="2"><path d="M10 8c6-4 14-4 20 0c2 8-2 24-5 24s-3-10-5-10s-2 10-5 10S8 16 10 8z"/><line x1="12" y1="16" x2="28" y2="16"/></svg>裏側矯正</div>
    <div class="nav-item"><svg width="40" height="40" viewBox="0 0 40 40" fill="none" stroke="#1f3557" stroke-width="2"><circle cx="20" cy="20" r="13"/><path d="M15 13l5 7l5-7M14 22h12M20 20v10"/></svg>費用</div>
  </nav>
  <div class="abs tel-box">
    <div class="tel-label">お電話でのご相談は下記より</div>
    <div class="tel-number"><svg width="30" height="30" viewBox="0 0 24 24" fill="#6fc0e0"><path d="M6.6 10.8a15 15 0 0 0 6.6 6.6l2.2-2.2a1 1 0 0 1 1-.25 11.4 11.4 0 0 0 3.6.57 1 1 0 0 1 1 1V20a1 1 0 0 1-1 1A17 17 0 0 1 3 4a1 1 0 0 1 1-1h3.5a1 1 0 0 1 1 1c0 1.25.2 2.45.57 3.6a1 1 0 0 1-.25 1z"/></svg>03-5512-4087</div>
  </div>
  <div class="abs quick-link quick-qa round"><svg width="30" height="30" viewBox="0 0 30 30" fill="none" stroke="#1f3557" stroke-width="2"><rect x="4" y="6" width="22" height="15" rx="4"/><path d="M10 21l-2 5l6-5"/></svg>Q&amp;A</div>
  <div class="abs quick-link quick-access round"><svg width="30" height="30" viewBox="0 0 24 24" fill="#1f3557"><path d="M12 2a7 7 0 0 0-7 7c0 5 7 13 7 13s7-8 7-13a7 7 0 0 0-7-7zm0 9.5A2.5 2.5 0 1 1 12 6.5a2.5 2.5 0 0 1 0 5z"/></svg>アクセス</div>
</header>

<h1 class="abs hero-copy"><span class="hl">マウスピース型矯正装置で</span><br>誰にも気づかれずに矯正治療</h1>

<table class="abs schedule">
  <thead><tr><th>診療時間</th><th>月</th><th>火</th><th>水</th><th>木</th><th>金</th><th>土</th><th>日</th></tr></thead>
  <tbody>
    <tr><td class="time">11:00〜14:00</td><td>○</td><td>○</td><td>○</td><td>○</td><td>○</td><td>○</td><td>-</td></tr>
    <tr><td class="time">16:00〜21:00</td><td>○</td><td>○</td><td>○</td><td>○</td><td>○</td><td>-</td><td>-</td></tr>
  </tbody>
</table>

<section>
  <div class="abs about-bg"></div>
  <h2 class="abs sec-title about-title"><span class="bar"></span>マウスピース型矯正装置（クリアフィット）<small>とは</small></h2>
  <div class="abs about-photo" role="img" aria-label="手のひらにのせた透明なマウスピース型矯正装置の写真"></div>
  <div class="abs about-text">
    <p>歯に固定されるワイヤーやブラケットを使わず、透明で取り外しができるプラスチックでできた装置を着用して矯正する方法がマウスピース矯正です。</p>
    <p>そんなマウスピース矯正には様々な種類がありますが、当院では独自のシステムで世界的に使用されているクリアフィットを中心に多く使用しています。</p>
    <p>裏側矯正にも力入れており、見えないMIX（マウスピース矯正と裏側矯正の組み合わせ）で幅広く対応できます。</p>
  </div>
  <h3 class="abs sec-title merit-title">マウスピース矯正の特徴・メリット</h3>
  <div class="abs merit-grid">
    <div class="merit"><div class="merit-photo" role="img" aria-label="透明なマウスピースの写真"></div><p>非常に目立ちにくい</p></div>
    <div class="merit"><div class="merit-photo" role="img" aria-label="マウスピースを取り外す様子の写真"></div><p>取り外して、食事ができる</p></div>
    <div class="merit"><div class="merit-photo" role="img" aria-label="歯ブラシで歯を磨く写真"></div><p>むし歯のリスクが減る</p></div>
    <div class="merit"><div class="merit-photo" role="img" aria-label="マウスピースを手に持つ写真"></div><p>金属によるアレルギーの心配がない</p></div>
    <div class="merit"><div class="merit-photo" role="img" aria-label="頬に手を当てる女性の写真"></div><p>痛みが少ない<br>（個人差があります）</p></div>
    <div class="merit"><div class="merit-photo" role="img" aria-label="3Dスキャナーのモニター画面の写真"></div><p>最新3Dスキャナーで治療のシミュレーション</p></div>
  </div>
  <div class="abs btn more-about">もっと詳しく<span>→</span></div>
</section>

<section>
  <h2 class="abs sec-title scanner-title"><svg width="60" height="60" viewBox="0 0 60 60" fill="none" stroke="#1f3557" stroke-width="2.5"><rect x="8" y="14" width="44" height="30" rx="3"/><line x1="22" y1="50" x2="38" y2="50"/><line x1="30" y1="44" x2="30" y2="50"/></svg><small>最新式デジタルスキャナー</small>　dento scope　<small>のご紹介</small></h2>
  <div class="abs scanner-photo" role="img" aria-label="デジタルスキャナー本体とモニターの写真"></div>
  <div class="abs scanner-text">
    <p>dento scope（口腔内スキャナ）は、口腔内をコンピューターに取り込むことが可能な、世界で最新鋭の3Dスキャニング装置です。従来では、シリコンの型取りで模型を作っていましたが、dento scopeでは、シリコンの型取りが不要なことを多くする必要があり、より精度の高い歯型を取ることができます。</p>
  </div>
  <div class="abs btn more-scanner">もっと詳しく<span>→</span></div>
</section>

<section>
  <div class="abs news-bg"></div>
  <h2 class="abs sec-title news-title"><svg width="46" height="46" viewBox="0 0 46 46" fill="none" stroke="#1f3557" stroke-width="2.5"><line x1="10" y1="36" x2="32" y2="8"/><line x1="8" y1="40" x2="38" y2="40"/></svg>新着情報</h2>
  <div class="abs news-list">
    <article class="post"><div class="post-thumb" role="img" aria-label="子どもの矯正に関する写真"></div><div class="post-body"><div class="post-date">2021.01.10</div>子供の矯正治療<br>どこで？</div></article>
    <article class="post"><div class="post-thumb" role="img" aria-label="歯列模型の写真"></div><div class="post-body"><div class="post-date">2021.01.03</div>矯正相談でよく聞かれること教えてもらいます</div></article>
    <article class="post"><div class="post-thumb logo" role="img" aria-label="医院名の画像"><div class="mark"></div><span>ルミエ矯正歯科</span></div><div class="post-body"><div class="post-date">2020.12.25</div>わかりにくい矯正歯科用語の解説と一般歯科医院の矯正歯科</div></article>
    <article class="post"><div class="post-thumb red" role="img" aria-label="裏側矯正装置の口腔内写真"></div><div class="post-body"><div class="post-date">2020.12.20</div>裏側矯正、ハーフリンガルの矯正歯科</div></article>
  </div>
  <div class="abs arrow" style="left:50px"><svg width="18" height="18" viewBox="0 0 18 18" fill="#fff"><path d="M12 2L4 9l8 7z"/></svg></div>
  <div class="abs arrow" style="left:1100px"><svg width="18" height="18" viewBox="0 0 18 18" fill="#fff"><path d="M6 2l8 7l-8 7z"/></svg></div>
  <div class="abs btn news-more">一覧はこちら<span>→</span></div>
</section>

<footer>
  <div class="abs foot-brand"><div class="brand-mark"></div><div class="brand-name">日本橋浜町ルミエ矯正歯科</div></div>
  <div class="abs foot-address">〒103-0099　東京都中央区日本橋みどり町2-4-8 3F</div>
  <div class="abs tel-number foot-tel" style="color:var(--navy)"><svg viewBox="0 0 24 24" fill="#1f3557"><path d="M6.6 10.8a15 15 0 0 0 6.6 6.6l2.2-2.2a1 1 0 0 1 1-.25 11.4 11.4 0 0 0 3.6.57 1 1 0 0 1 1 1V20a1 1 0 0 1-1 1A17 17 0 0 1 3 4a1 1 0 0 1 1-1h3.5a1 1 0 0 1 1 1c0 1.25.2 2.45.57 3.6a1 1 0 0 1-.25 1z"/></svg>03-5512-4087</div>
  <div class="abs cta" style="left:590px">矯正相談はこちら<span>→</span></div>
  <div class="abs cta" style="left:890px">初診予約はこちら<span>→</span></div>
  <div class="abs map" role="img" aria-label="医院周辺の地図"></div>
  <div class="abs footer">
    <div class="footer-nav"><span>医院紹介</span><span>治療内容</span><span>マウスピース矯正</span><span>部分矯正</span><span>裏側矯正</span><span>費用</span><span>Q&amp;A</span><span>アクセス</span></div>
    <div class="footer-mark"></div>
    <div class="copy">Copyright © 2021 日本橋浜町ルミエ矯正歯科　見えない歯列矯正　子供・大人の矯正 All rights Reserved.</div>
  </div>
</footer>

</body>
</html>
```